Sales Brochure

Industrial brochure of my industrial pump business which includes repair and sales of equipment. I distribute and repair industrial pumps for the midwest market. Design color is blue.

```html
<!DOCTYPE html>
<html lang="en">
<head>
<meta charset="utf-8">
<title>Northfield Pump – Sales Brochure</title>
<link href="https://fonts.googleapis.com/css2?family=Poppins:wght@400;500;600;700&display=swap" rel="stylesheet">
<style>
  :root{
    --blue:#4a78d0;
    --blue-light:#7fa6ea;
    --blue-pale:#a9c6f2;
    --ink:#1f1f1f;
    --dark:#323334;
    --white:#ffffff;
    --stage:#e6e6e6;
  }
  *{box-sizing:border-box;margin:0;padding:0}
  html,body{width:1200px;height:397px;overflow:hidden;background:var(--stage);font-family:"Poppins",sans-serif;color:var(--ink)}
  .spread{position:relative;width:1200px;height:397px}
  .page{position:absolute;top:20px;width:257px;height:357px;background:var(--white);overflow:hidden;box-shadow:0 2px 6px rgba(0,0,0,.18)}
  .page--front{left:331px}
  .page--back{left:612px}
  .abs{position:absolute}
  .photo{position:absolute}

  /* front */
  .brand{left:18px;top:20px;display:flex;align-items:center;gap:5px}
  .brand__dot{width:18px;height:18px;border-radius:50%;background:var(--blue)}
  .brand__name{font-weight:700;font-size:12px;color:var(--blue);letter-spacing:.2px}
  .brand__web{left:45px;top:42px;font-size:6px;color:var(--blue);font-style:normal}
  .header-photo{left:150px;top:0;width:107px;height:65px;background:linear-gradient(135deg,#dfe8fb 0%,#7aa3ec 45%,#3a6fd6 100%)}
  .dark-band{left:0;top:65px;width:257px;height:116px;background:var(--dark)}
  .band-photo{left:150px;top:65px;width:107px;height:116px;background:linear-gradient(120deg,#3e3f42 0%,#2a3270 55%,#2b3c96 100%)}
  .headline{left:18px;top:82px;color:var(--white);font-weight:700;font-size:14px;line-height:15px}
  .headline .sub{display:block;font-weight:400;font-size:9.5px;line-height:12px;margin-top:1px}
  .headline .accent{display:block;color:var(--blue-light);font-size:14px;line-height:15px;margin-top:1px}
  .side-column{left:135px;top:158px;width:103px;height:199px;background:var(--blue-light)}
  .product-frame{left:142px;width:90px;height:55px;background:var(--white);padding:4px}
  .product-frame .photo{position:static;width:100%;height:100%}
  .section-title{font-weight:600;font-size:9px;color:var(--blue)}
  .body-text{font-size:5.2px;line-height:8px;color:var(--ink)}
  .vision{left:18px;top:203px;width:104px}
  .vision .body-text{margin-top:3px}
  .service-bar{left:0;top:295px;width:257px;height:23px;background:var(--dark);color:var(--blue-light);font-size:8px;display:flex;align-items:center;justify-content:center;gap:3px;white-space:nowrap}
  .service-bar b{color:var(--white);font-weight:600}
  .call-left{left:0;top:318px;width:135px;height:39px;display:flex;align-items:center;justify-content:center;font-size:9.5px}
  .call-right{left:135px;top:318px;width:103px;height:39px;background:var(--blue);color:var(--white);display:flex;align-items:center;justify-content:center;gap:4px;font-weight:600;font-size:10px}

  /* back */
  .products{left:19px;top:16px;width:215px}
  .products .body-text{margin-top:2px;font-size:5px;line-height:8px}
  .blue-band{left:0;top:65px;width:257px;height:116px;background:linear-gradient(90deg,var(--blue) 0%,#6c96e2 60%,var(--blue-pale) 100%)}
  .headline--back{left:19px;top:81px;font-size:16px;line-height:18px}
  .headline--back .sub{font-size:10px;margin-top:3px}
  .hero-photo{left:145px;top:75px;width:92px;height:100px;border-radius:4px;background:linear-gradient(160deg,#d7383e 0%,#b8232a 60%,#8f1a20 100%)}
  .pump-frame{left:19px;top:158px;width:109px;height:62px;background:var(--white);border:1.5px solid var(--blue);padding:5px}
  .pump-frame .photo{position:static;width:100%;height:100%}
  .timing{left:19px;top:227px;width:109px;height:53px;border:1.3px solid var(--ink);text-align:center;padding-top:4px}
  .timing__label{font-size:7px;font-weight:500;color:var(--blue);letter-spacing:1px;display:flex;align-items:center;justify-content:center;gap:3px}
  .timing__days{font-size:8.5px;font-weight:500;line-height:10px}
  .timing__hours{font-size:4.8px;color:var(--blue);line-height:6px}
  .expertise{left:140px;top:203px;width:100px}
  .expertise .body-text{margin-top:3px}
  .call-bar{left:0;top:295px;width:257px;height:23px;background:var(--dark);display:flex;align-items:center;justify-content:center;gap:10px;color:var(--blue-light);font-size:9px}
  .call-bar b{color:var(--white);font-weight:600;font-size:10px;display:flex;align-items:center;gap:4px}
  .web-bar{left:0;top:318px;width:257px;height:39px;background:linear-gradient(90deg,var(--blue),var(--blue-pale));color:var(--white);display:flex;align-items:center;justify-content:center;font-size:7.5px}
</style>
</head>
<body>
<main class="spread">

  <section class="page page--front">
    <div class="photo header-photo" role="img" aria-label="Close-up of blue industrial pump parts"></div>
    <div class="abs brand"><span class="brand__dot"></span><span class="brand__name">NORTHFIELD PUMP</span></div>
    <span class="abs brand__web">www.northfieldpump.com</span>

    <div class="abs dark-band"></div>
    <div class="photo band-photo" role="img" aria-label="Dark blue cast-iron pump in a workshop"></div>
    <h1 class="abs headline">OUR INDUSTRIAL<br>EQUIPMENT<span class="sub">KEEPS YOUR BUSINESS</span><span class="accent">MOVING<br>FORWARD</span></h1>

    <div class="abs side-column"></div>
    <div class="abs product-frame" style="top:168px"><div class="photo" role="img" aria-label="White diaphragm pump" style="background:linear-gradient(135deg,#eef0f3 0%,#c3c8cf 55%,#8d939c 100%)"></div></div>
    <div class="abs product-frame" style="top:228px"><div class="photo" role="img" aria-label="Blue split-case centrifugal pump" style="background:linear-gradient(135deg,#8cc0f2 0%,#4f9be6 50%,#2d6fc4 100%)"></div></div>

    <div class="abs vision">
      <h2 class="section-title">Our Vision</h2>
      <p class="body-text">At Northfield Pump, our vision is to be the leading provider of industrial equipment in the country. We are committed to providing our clients with the highest quality products and services to help them succeed and grow. We will achieve this by staying at the forefront of industry trends and by continuously improving our offerings.</p>
    </div>

    <div class="abs service-bar">We offer <b>Repair Services</b> for all the <b>Equipment We Sell</b></div>
    <div class="abs call-left">CALL US TODAY!</div>
    <div class="abs call-right">
      <svg width="9" height="9" viewBox="0 0 24 24"><path d="M6.6 10.8a15 15 0 0 0 6.6 6.6l2.2-2.2a1 1 0 0 1 1-.25 11.4 11.4 0 0 0 3.6.57 1 1 0 0 1 1 1V20a1 1 0 0 1-1 1A17 17 0 0 1 3 4a1 1 0 0 1 1-1h3.5a1 1 0 0 1 1 1c0 1.25.2 2.450.57 3.57a1 1 0 0 1-.25 1z" fill="#fff"/></svg>
      555-014-7720
    </div>
  </section>

  <section class="page page--back">
    <div class="abs products">
      <h2 class="section-title">Our Products</h2>
      <p class="body-text">We offer a comprehensive range of industrial equipment, including pumps, motors, and power transmission products . All of our products are sourced from trusted brands and are of the highest quality. We are dedicated to providing our clients with reliable, durable, and efficient equipment.</p>
    </div>

    <div class="abs blue-band"></div>
    <div class="photo hero-photo" role="img" aria-label="Red vertical turbine pump"></div>
    <h1 class="abs headline headline--back">EFFICIENCY,<br>RELIABILITY,<br>RESULTS<span class="sub">INDUSTRIAL PUMPS</span></h1>

    <div class="abs pump-frame"><div class="photo" role="img" aria-label="Grey vertical sump pump" style="background:linear-gradient(135deg,#c5ccd4 0%,#8a96a3 55%,#5b6673 100%)"></div></div>

    <div class="abs timing">
      <div class="timing__label">
        <svg width="8" height="8" viewBox="0 0 16 16"><circle cx="8" cy="8" r="6.5" fill="none" stroke="#4a78d0" stroke-width="1.4"/><path d="M8 4v4.5l2.5 1.5" fill="none" stroke="#4a78d0" stroke-width="1.4"/></svg>
        TIMING
      </div>
      <div class="timing__days">Monday - Friday</div>
      <div class="timing__hours">8:00am - 5:00pm</div>
      <div class="timing__days">Saturday - Sunday</div>
      <div class="timing__hours">Closed</div>
    </div>

    <div class="abs expertise">
      <h2 class="section-title">Our Expertise</h2>
      <p class="body-text">With over 78 years of combined experience in the industrial equipment industry, the team at Northfield Pump has the knowledge and expertise to help you find the right equipment for your business needs. We offer expert advice, personalized service, and ongoing support to ensure your complete satisfaction.</p>
    </div>

    <div class="abs call-bar">CALL US TODAY!
      <b><svg width="9" height="9" viewBox="0 0 24 24"><path d="M6.6 10.8a15 15 0 0 0 6.6 6.6l2.2-2.2a1 1 0 0 1 1-.25 11.4 11.4 0 0 0 3.6.57 1 1 0 0 1 1 1V20a1 1 0 0 1-1 1A17 17 0 0 1 3 4a1 1 0 0 1 1-1h3.5a1 1 0 0 1 1 1c0 1.25.2 2.45.57 3.57a1 1 0 0 1-.25 1z" fill="#fff"/></svg>555-014-7720</b>
    </div>
    <div class="abs web-bar">www.northfieldpump.com</div>
  </section>

</main>
</body>
</html>
```